Business Card Design for Telecommunications and IT Solutions company "OKRA"

BC for telecommunications company name "OKRA" with slogan "Telecom & IT Solutions"

should have the full name as above "OKRA" and the slogan
color reqiured black, red (dark) and white

simple, professional, serious, modern design is required

1 side of business card have a full details, contacts and logo
other side have only the logo, website and full company name "ALOKRA Company for Telecommunications service & Information Technology LLC"

i have attached the logo and current business card sample and note that the logo was changed not the same in the attached business card

Industry/Entity Type

Telecommunications

Contact Information for Business Card

Full name: Omar Nabil Al Hudari
Job title: General Manager
Mobile no: +964xxxxxxxxx
email: omar@okra-tel.example
full name of the company: ALOKRA Company Telecommunications Services & Information Technology LLC.
website: www.okra-tel.example
address: Nakheel Dist. 148/7 JubailaQadim, Basra, Iraq

Requirements
Must have
• two languages in the same side of business card (English, Arabic) for only the name and title

```html
<!DOCTYPE html>
<html lang="en">
<head>
<meta charset="utf-8">
<title>OKRA Telecom &amp; IT Solutions – Business Card</title>
<link rel="stylesheet" href="https://fonts.googleapis.com/css2?family=Poppins:ital,wght@0,400;0,600;1,600&family=Cairo:wght@400;600&display=swap">
<style>
  :root {
    --ink: #232323;
    --charcoal: #262626;
    --crimson: #a4161a;
    --paper: #f4f4f4;
    --white: #ffffff;
    --muted: #6b6b6b;
    --stage: #e6e6e4;
  }
  * { box-sizing: border-box; margin: 0; padding: 0; }
  html, body {
    width: 1200px; height: 900px; overflow: hidden;
    background: var(--stage);
    font-family: "Poppins", sans-serif;
  }
  .canvas {
    width: 1200px; height: 900px;
    display: flex; flex-direction: column; align-items: center; justify-content: center;
    gap: 40px;
  }
  .card {
    position: relative; width: 630px; height: 360px;
    background: var(--paper); overflow: hidden;
    box-shadow: 0 6px 18px rgba(0,0,0,.18);
  }
  .arabic { font-family: "Cairo", sans-serif; direction: rtl; unicode-bidi: isolate; }

  /* brand lockup */
  .brand { display: flex; flex-direction: column; align-items: center; }
  .brand-name {
    font-weight: 600; color: var(--ink); letter-spacing: 2px; line-height: 1;
    display: flex; align-items: center; gap: 10px;
  }
  .brand-dot { width: 14px; height: 14px; border-radius: 50%; background: var(--crimson); }
  .brand-slogan {
    font-size: 9px; letter-spacing: 1.4px; color: var(--ink); text-transform: uppercase; margin-top: 4px;
  }

  /* back side */
  .card-back { display: flex; flex-direction: column; align-items: center; justify-content: center; text-align: center; }
  .card-back .brand-name { font-size: 54px; }
  .company-lines { margin-top: 22px; color: var(--ink); font-size: 11.5px; line-height: 1.65; }
  .company-lines .arabic { font-size: 11px; color: var(--muted); }
  .website-back { margin-top: 10px; color: var(--crimson); font-weight: 600; font-size: 13px; }

  /* front side */
  .card-front .sweep { position: absolute; inset: 0; width: 100%; height: 100%; }
  .card-front .brand { position: absolute; left: 290px; top: 42px; }
  .card-front .brand-name { font-size: 44px; }
  .details { position: absolute; left: 44px; top: 150px; color: var(--white); }
  .person { font-size: 16px; font-weight: 600; font-style: italic; display: flex; gap: 8px; align-items: baseline; }
  .person .arabic { font-style: normal; font-size: 15px; }
  .role { font-size: 12px; margin-top: 4px; display: flex; gap: 6px; align-items: baseline; }
  .role .arabic { font-size: 12px; }
  .address { font-size: 12.5px; margin-top: 8px; letter-spacing: .3px; }
  .contacts { display: flex; gap: 16px; margin-top: 12px; font-size: 12.5px; }
  .contact { display: flex; align-items: center; gap: 6px; }
  .contact svg { width: 13px; height: 13px; flex: none; }
</style>
</head>
<body>
<main class="canvas">

  <section class="card card-back" aria-label="Business card back">
    <div class="brand">
      <div class="brand-name"><span class="brand-dot"></span>OKRA</div>
      <div class="brand-slogan">Telecom &amp; IT Solutions</div>
    </div>
    <div class="company-lines">
      <p>ALOKRA Company <span class="arabic">شركة العكرة</span></p>
      <p>Telecommunications Services &amp; Information Technology LLC.</p>
      <p class="arabic">شركة العكرة لخدمات الاتصالات وتقنية المعلومات</p>
    </div>
    <p class="website-back">www.okra-tel.example</p>
  </section>

  <section class="card card-front" aria-label="Business card front">
    <svg class="sweep" viewBox="0 0 630 360" preserveAspectRatio="none" aria-hidden="true">
      <path d="M0,82 Q330,108 630,238 L630,360 L0,360 Z" fill="var(--crimson)"/>
      <path d="M0,104 Q330,132 630,262 L630,360 L0,360 Z" fill="var(--charcoal)"/>
    </svg>

    <div class="brand">
      <div class="brand-name"><span class="brand-dot"></span>OKRA</div>
      <div class="brand-slogan">Telecom &amp; IT Solutions</div>
    </div>

    <div class="details">
      <p class="person">Omar Nabil Al Hudari / <span class="arabic">عمر نبيل الحضري</span></p>
      <p class="role">General Manager / <span class="arabic">المدير العام</span></p>
      <p class="address">Nakheel Dist. 148/7 JubailaQadim, Basra, Iraq</p>
      <div class="contacts">
        <span class="contact">
          <svg viewBox="0 0 16 16" aria-hidden="true"><path d="M4 1h3l1 4-2 1a9 9 0 0 0 4 4l1-2 4 1v3a2 2 0 0 1-2 2A13 13 0 0 1 2 3a2 2 0 0 1 2-2z" fill="var(--crimson)"/></svg>
          +964xxxxxxxxx
        </span>
        <span class="contact">
          <svg viewBox="0 0 16 16" aria-hidden="true"><rect x="1" y="3" width="14" height="10" rx="1" fill="var(--crimson)"/><path d="M1.5 3.5 8 9l6.5-5.5" stroke="var(--charcoal)" stroke-width="1.4" fill="none"/></svg>
          omar@okra-tel.example
        </span>
        <span class="contact">
          <svg viewBox="0 0 16 16" aria-hidden="true"><circle cx="8" cy="8" r="7" fill="var(--crimson)"/><path d="M1 8h14M8 1c-3 3-3 11 0 14M8 1c3 3 3 11 0 14" stroke="var(--charcoal)" stroke-width="1.2" fill="none"/></svg>
          www.okra-tel.example
        </span>
      </div>
    </div>
  </section>

</main>
</body>
</html>
```